TAVRO Capital Group LLC a High Risk Big Rewards company for Rich Young Entrepreneurs

We would like a very modern, powerful in the eyes of our customers, modern, minimalist feel, financial gain. this business card is for young Rich entrepreneurs who want to invest money into High Risk, Big Rewards Businesses. The card Should sell the business!! let your creativity go Wild! I pick most of the designers for this project because of your BOLD Designs, I would like this card to be Bold, Modern, Minimalist, use as many effects in your graphic Artist Mind, Do not let the Financial sound of this business to make you think Conservative that's the last thing we are! if you have a lot of money and you want to play a risky market call US
Updates

Project Deadline Extended
Reason: have not received, enough designs to choose 1st and second place, sure I have received over 100 designs but it seems most designers are submitting every card they have ever made before and calling it mine, please we are looking for fresh ideas please!

Target Market(s)

Private Risky Investors

Industry/Entity Type

Financial

Contact Information for Business Card

powerful in the eyes of our customers,modern, minimalist feel

Font styles to use
Other font styles liked:
• Modern feeling fonts

Requirements
Must have
• The Company Name is TAVRO Capital Group LLC and it must be on the CARD
• My Name, title, Cell , email
• Delvin Ashcroft G.E.D.
• Managing Member
• 555.038.6195
• delvin@tavrocapitalgroup.example
Nice to have
• try a black thick plastic card with round corners with Delvin Ashcroft GED (make sure GED is smaller than name) just on one side of the card, and my phone number with out the icons and email on the other side, this card should look like a exclusive credit card or exclusive VIP card, something you would never loose

```html
<!DOCTYPE html>
<html lang="en">
<head>
<meta charset="utf-8">
<title>TAVRO Capital Group LLC – Business Card</title>
<link href="https://fonts.googleapis.com/css2?family=Exo+2:wght@300;400;500;700&display=swap" rel="stylesheet">
<style>
  :root {
    --page: #ffffff;
    --stage: #0d0d0d;
    --card-dark: #1c1c1c;
    --card-mid: #4a4a4a;
    --card-light: #7a7a7a;
    --band: #0b0b0b;
    --ink: #ffffff;
    --ink-soft: #e8e8e8;
    --ghost: rgba(255,255,255,0.28);
    --edge: rgba(255,255,255,0.35);
  }
  * { margin: 0; padding: 0; box-sizing: border-box; }
  html, body {
    width: 1200px; height: 1200px; overflow: hidden;
    background: var(--page);
    font-family: "Exo 2", sans-serif;
  }
  .stage {
    position: absolute; left: 35px; top: 42px; width: 1117px; height: 1118px;
    background: var(--stage);
  }
  .card {
    position: absolute; left: 272px; width: 644px; height: 404px;
    border-radius: 18px; overflow: hidden;
    border: 1px solid var(--edge);
    box-shadow: 0 4px 10px rgba(0,0,0,0.7);
  }
  .card-front { top: 160px; }
  .card-back  { top: 657px; }
  .card-surface {
    position: absolute; inset: 0;
    background:
      radial-gradient(ellipse 60% 70% at 62% 40%, var(--card-light) 0%, var(--card-mid) 45%, var(--card-dark) 100%);
  }
  .card-gloss {
    position: absolute; inset: 0;
    background: linear-gradient(180deg, rgba(255,255,255,0.10) 0%, rgba(255,255,255,0) 40%, rgba(0,0,0,0.15) 100%);
  }
  .edge-flare { position: absolute; left: 0; top: 0; }
  .brand {
    position: absolute; color: var(--ink); font-weight: 500; line-height: 1;
  }
  .brand-front { left: 44px; top: 42px; }
  .brand-name { display: block; font-size: 82px; letter-spacing: 2px; }
  .brand-sub { display: block; font-size: 27px; margin-top: 8px; letter-spacing: 0.5px; }
  .brand-rule {
    position: absolute; left: 46px; top: 165px; width: 222px; height: 1px; background: var(--ink-soft);
  }
  .name-band {
    position: absolute; left: 0; top: 287px; width: 100%; height: 51px;
    background: linear-gradient(90deg, rgba(30,30,30,0.7) 0%, var(--band) 45%, var(--band) 100%);
    border-top: 1px solid rgba(255,255,255,0.25);
    border-bottom: 1px solid rgba(255,255,255,0.15);
  }
  .holder-name {
    position: absolute; right: 56px; top: 297px;
    color: var(--ink); font-size: 28px; font-weight: 400; letter-spacing: 1px; white-space: nowrap;
  }
  .holder-credential { font-size: 18px; margin-left: 6px; letter-spacing: 1px; }
  .holder-title {
    position: absolute; right: 58px; top: 340px;
    color: var(--ink-soft); font-size: 18px; font-weight: 400; letter-spacing: 1.5px;
  }
  .brand-ghost {
    position: absolute; left: 0; width: 100%; top: 52px; text-align: center;
    color: var(--ghost); font-weight: 500; line-height: 1;
  }
  .brand-ghost .brand-name { font-size: 110px; letter-spacing: 3px; }
  .brand-ghost .brand-sub { font-size: 36px; margin-top: 12px; }
  .contact {
    position: absolute; left: 0; width: 100%; top: 304px; text-align: center;
    color: var(--ink); font-weight: 400; letter-spacing: 2px; line-height: 27px;
  }
  .contact-phone { font-size: 20px; }
  .contact-email { font-size: 20px; letter-spacing: 1.6px; }
</style>
</head>
<body>
  <div class="stage"></div>

  <section class="card card-front">
    <div class="card-surface" role="img" aria-label="Dark graphite card surface with faint geometric triangle pattern and soft light spots"></div>
    <div class="card-gloss"></div>
    <svg class="edge-flare" width="644" height="404" viewBox="0 0 644 404">
      <defs>
        <linearGradient id="flareTop" x1="0" x2="1">
          <stop offset="0" stop-color="#fff" stop-opacity="0"/>
          <stop offset="0.5" stop-color="#fff" stop-opacity="0.9"/>
          <stop offset="1" stop-color="#fff" stop-opacity="0"/>
        </linearGradient>
      </defs>
      <rect x="120" y="0" width="420" height="2" fill="url(#flareTop)"/>
      <rect x="180" y="402" width="420" height="2" fill="url(#flareTop)"/>
    </svg>
    <div class="brand brand-front">
      <span class="brand-name">TAVRO</span>
      <span class="brand-sub">Capital Group LLC</span>
    </div>
    <div class="name-band"></div>
    <div class="holder-name">Delvin Ashcroft<span class="holder-credential">GED</span></div>
    <div class="holder-title">Managing Member</div>
  </section>

  <section class="card card-back">
    <div class="card-surface" role="img" aria-label="Dark graphite card surface with faint geometric triangle pattern and soft light spots"></div>
    <div class="card-gloss"></div>
    <svg class="edge-flare" width="644" height="404" viewBox="0 0 644 404">
      <defs>
        <linearGradient id="flareBack" x1="0" x2="1">
          <stop offset="0" stop-color="#fff" stop-opacity="0"/>
          <stop offset="0.5" stop-color="#fff" stop-opacity="0.9"/>
          <stop offset="1" stop-color="#fff" stop-opacity="0"/>
        </linearGradient>
      </defs>
      <rect x="150" y="0" width="400" height="2" fill="url(#flareBack)"/>
      <rect x="180" y="402" width="420" height="2" fill="url(#flareBack)"/>
    </svg>
    <div class="brand-ghost">
      <span class="brand-name">TAVRO</span>
      <span class="brand-sub">Capital Group LLC</span>
    </div>
    <div class="contact">
      <div class="contact-phone">555.038.6195</div>
      <div class="contact-email">delvin@tavrocapitalgroup.example</div>
    </div>
  </section>
</body>
</html>
```